International Freight Forwarder need a business card

We need a logo design for a freight forwarding company . We are active in Sea Transportation, Truck transportation, and Air Transportation, The design should be have normal dimensions of a card and should not have cuts and holes in its design (printed design is required - lamination accepted)

The said company is agent and sales representative of 2 other Shipping companies (whose logos, name, and website should also be mentioned on the card)

Industry/Entity Type

Logistics

Contact Information for Business Card

Address is "No.7, 2nd Darvish Kuche-ye-Sarvestani, Tehran, IR
Tel number is +98 21 66342819
Fax number is +98 21 66349527
E-Mail address is info@sarvnamavaran.com
Website is www.sarvnamavaran.com

Open Layer Logos attached as well

Colors
33a6d7
0292cd
0255a3
3276b5
85abd2
85cae6
cee9f5
d5e2ee
ffffff

Requirements
Must have
• Main logo of Sarvnama Varan
• Logo of KDR Shipping Line
• London, United Kingdom
• kdrline.com
• Logo of Coral Tide Shipping
• Dubai, United Arab Emirates
• ctsuae.com
• We require OPEN layer file to be submitted to us upon project selection.
Should not have
• Weird Designs such as cuts to the shape or holes in design.

```html
<!DOCTYPE html>
<html lang="en">
<head>
<meta charset="utf-8">
<title>Sarvnama Varan – Business Card</title>
<link rel="stylesheet" href="https://fonts.googleapis.com/css2?family=Roboto:wght@400;500&display=swap">
<style>
  :root {
    --bg: #e9edf1;
    --card: #ffffff;
    --navy: #2b4a8e;
    --deep-blue: #0255a3;
    --sky: #33a6d7;
    --text: #3c3c3c;
    --icon: #4a5a78;
    --rule: #2b4a8e;
  }
  * { box-sizing: border-box; margin: 0; padding: 0; }
  html, body { width: 1200px; height: 1200px; overflow: hidden; }
  body {
    background: var(--bg);
    font-family: "Roboto", sans-serif;
    color: var(--text);
    position: relative;
  }
  .card {
    position: absolute;
    left: 214px;
    width: 772px;
    height: 438px;
    background: var(--card);
    border-radius: 20px;
    box-shadow: 0 4px 14px rgba(0,0,0,0.18);
  }
  .card--front { top: 151px; }
  .card--back { top: 633px; }

  /* Front */
  .brand {
    position: absolute;
    left: 100px;
    top: 92px;
    width: 180px;
    text-align: center;
  }
  .brand__circle {
    width: 150px;
    height: 150px;
    margin: 0 auto 18px;
    border-radius: 50%;
    border: 3px solid var(--navy);
  }
  .brand__name {
    font-size: 16px;
    font-weight: 500;
    line-height: 1.3;
    color: var(--navy);
  }
  .divider {
    position: absolute;
    width: 2px;
    background: var(--rule);
  }
  .card--front .divider { left: 335px; top: 102px; height: 238px; }
  .contact {
    position: absolute;
    left: 369px;
    top: 86px;
  }
  .contact__name {
    font-size: 29px;
    font-weight: 500;
    color: var(--navy);
    line-height: 1.1;
  }
  .contact__role {
    font-size: 20px;
    margin-top: 4px;
  }
  .contact__address {
    font-size: 18px;
    line-height: 26px;
    margin-top: 26px;
  }
  .contact__list {
    list-style: none;
    margin-top: 16px;
    font-size: 18px;
  }
  .contact__list li {
    display: flex;
    align-items: center;
    height: 27.5px;
  }
  .contact__list svg { width: 17px; height: 17px; margin-right: 7px; flex: none; }

  /* Back */
  .card--back .divider { left: 387px; top: 132px; height: 174px; }
  .partner {
    position: absolute;
    top: 130px;
  }
  .partner__mark {
    display: flex;
    align-items: center;
    gap: 18px;
  }
  .partner__circle {
    width: 104px;
    height: 104px;
    border-radius: 50%;
    flex: none;
  }
  .partner__name {
    font-size: 21px;
    font-weight: 500;
    line-height: 1.2;
  }
  .partner--coral { left: 78px; width: 282px; }
  .partner--coral .partner__circle { background: var(--deep-blue); }
  .partner--coral .partner__name { color: var(--navy); }
  .partner--kdr { left: 412px; width: 300px; }
  .partner--kdr .partner__circle { border: 4px solid var(--sky); }
  .partner--kdr .partner__name { color: var(--sky); }
  .partner__info {
    list-style: none;
    margin-top: 26px;
    font-size: 19px;
  }
  .partner__info li {
    display: flex;
    align-items: center;
    height: 28px;
    gap: 6px;
  }
  .partner--coral .partner__info li { justify-content: flex-end; }
  .partner__info svg { width: 17px; height: 17px; flex: none; }
  .partner--coral .partner__info svg { color: var(--navy); }
  .partner--kdr .partner__info svg { color: var(--sky); }
</style>
</head>
<body>

<section class="card card--front">
  <div class="brand">
    <div class="brand__circle"></div>
    <p class="brand__name">Sarvnama Varan<br>International<br>Transport.Co L.L.c</p>
  </div>

  <div class="divider"></div>

  <div class="contact">
    <h1 class="contact__name">Daniel Harrow</h1>
    <p class="contact__role">President &amp; CEO</p>
    <p class="contact__address">No.7, 2nd Darvish<br>Kuche-ye-Sarvestani, Tehran, IR</p>
    <ul class="contact__list">
      <li>
        <svg viewBox="0 0 24 24" fill="none" stroke="#4a5a78" stroke-width="1.8"><path d="M5 3h4l2 5-2.5 1.5a11 11 0 0 0 6 6L16 13l5 2v4a2 2 0 0 1-2 2A17 17 0 0 1 3 5a2 2 0 0 1 2-2z"/></svg>
        +98 21 66342819
      </li>
      <li>
        <svg viewBox="0 0 24 24" fill="#4a5a78"><rect x="6" y="2" width="12" height="6"/><rect x="2" y="9" width="20" height="9" rx="2"/><rect x="6" y="15" width="12" height="7" fill="#fff" stroke="#4a5a78" stroke-width="2"/></svg>
        +98 21 66349527
      </li>
      <li>
        <svg viewBox="0 0 24 24" fill="none" stroke="#4a5a78" stroke-width="1.8"><rect x="2" y="5" width="20" height="14"/><path d="M2 5l10 8 10-8"/></svg>
        info@sarvnamavaran.com
      </li>
      <li>
        <svg viewBox="0 0 24 24" fill="none" stroke="#4a5a78" stroke-width="1.8"><circle cx="12" cy="12" r="10"/><path d="M2 12h20M12 2c3 3 3 17 0 20M12 2c-3 3-3 17 0 20"/></svg>
        www.sarvnamavaran.com
      </li>
    </ul>
  </div>
</section>

<section class="card card--back">
  <div class="partner partner--coral">
    <div class="partner__mark">
      <div class="partner__circle"></div>
      <p class="partner__name">Coral Tide<br>Shipping LLC</p>
    </div>
    <ul class="partner__info">
      <li>Dubai, United Arab Emirates
        <svg viewBox="0 0 24 24" fill="none" stroke="currentColor" stroke-width="2"><path d="M12 22s7-7 7-12a7 7 0 0 0-14 0c0 5 7 12 7 12z"/><circle cx="12" cy="10" r="2.5"/></svg>
      </li>
      <li>www.ctsuae.com
        <svg viewBox="0 0 24 24" fill="none" stroke="currentColor" stroke-width="1.8"><circle cx="12" cy="12" r="10"/><path d="M2 12h20M12 2c3 3 3 17 0 20M12 2c-3 3-3 17 0 20"/></svg>
      </li>
    </ul>
  </div>

  <div class="divider"></div>

  <div class="partner partner--kdr">
    <div class="partner__mark">
      <div class="partner__circle"></div>
      <p class="partner__name">KDR<br>Shipping Line Ltd</p>
    </div>
    <ul class="partner__info">
      <li>
        <svg viewBox="0 0 24 24" fill="none" stroke="currentColor" stroke-width="2"><path d="M12 22s7-7 7-12a7 7 0 0 0-14 0c0 5 7 12 7 12z"/><circle cx="12" cy="10" r="2.5"/></svg>
        London, United Kingdom
      </li>
      <li>
        <svg viewBox="0 0 24 24" fill="none" stroke="currentColor" stroke-width="1.8"><circle cx="12" cy="12" r="10"/><path d="M2 12h20M12 2c3 3 3 17 0 20M12 2c-3 3-3 17 0 20"/></svg>
        www.kdrline.com
      </li>
    </ul>
  </div>
</section>

</body>
</html>
```